Security based company delivering High Risk Training to Law Enforcement Agencies Worldwide.

We need a Web design for a company doing business in Washington D.C. We deliver High Risk Training to Law Enforcement Agencies throughout the world. Our focus is on Improvised Explosive Devices. We train Bomb Technicians and First Responders in all aspects relating to bombings and criminal incidents globally.
Updates

Reason: We have uploaded our logo. Thank you.

Target Market(s)

Military and Law Enforcement Personnel from around the world.

Industry/Entity Type

Business

Requirements
Should not have
• Do not include cartoon like characters.

```html
<!DOCTYPE html>
<html lang="en">
<head>
<meta charset="utf-8">
<title>Vortan Tactical — High Risk Training</title>
<link href="https://fonts.googleapis.com/css2?family=Exo:wght@400;500;600;700;800&display=swap" rel="stylesheet">
<style>
:root{
  --navy:#0a185e;
  --navy-dark:#050e44;
  --green:#8cc63f;
  --green-soft:#8ec54a;
  --light:#f0f0f0;
  --grey-text:#8a8a8a;
  --grey-title:#6e6e6e;
  --btn-grey:#d9d9d9;
  --charcoal:#333333;
  --ink:#1e1e1e;
  --white:#ffffff;
}
*{box-sizing:border-box;margin:0;padding:0}
html,body{width:677px;height:1200px;overflow:hidden}
body{font-family:'Exo',sans-serif;background:var(--light);position:relative;color:var(--ink)}
.abs{position:absolute}

/* header */
.site-header{left:0;top:0;width:677px;height:64px;background:linear-gradient(180deg,var(--navy-dark),var(--navy))}
.brand{left:32px;top:14px;color:var(--white);font-weight:800;font-size:17px;line-height:17px;letter-spacing:.5px}
.main-nav{right:29px;top:23px;display:flex;gap:10px}
.main-nav a{color:var(--white);text-decoration:none;font-weight:600;font-size:14px}
.main-nav a.active{color:var(--green)}

/* hero */
.hero{left:0;top:64px;width:677px;height:254px}
.hero-photo{width:100%;height:100%;background:linear-gradient(180deg,#c9ccce 0%,#d8d6d0 45%,#c7b59a 75%,#b9a07c 100%)}
.hero-caption{left:361px;top:141px;width:287px;height:105px;background:rgba(140,198,63,.9);color:var(--white);font-weight:700;font-size:13.5px;line-height:20px;text-align:right;padding:12px 16px 0 10px}
.hero-arrow{top:273px;width:24px;height:23px;background:rgba(255,255,255,.85)}
.hero-arrow.prev{left:596px}
.hero-arrow.next{left:626px}

/* features */
.feature{top:352px;width:170px}
.feature h3{font-weight:500;font-size:12.5px;color:var(--grey-title);margin-bottom:4px}
.feature p{font-size:10px;line-height:13.4px;color:var(--grey-text)}
.more-btn{display:block;width:69px;height:20px;margin-top:9px;background:var(--btn-grey);color:var(--white);font-weight:600;font-size:11px;line-height:20px;text-align:center}
.more-btn.primary{background:var(--green-soft)}

/* showcase */
.showcase{left:0;top:495px;width:677px;height:239px;background:var(--charcoal);border-bottom:2px solid var(--green)}
.showcase-title{left:49px;top:22px;color:var(--white);font-weight:600;font-size:12px}
.showcase-nav{top:20px}
.showcase-item{top:57px;width:256px}
.showcase-photo{width:256px;height:90px;border:2px solid var(--white)}
.photo-blast{background:linear-gradient(180deg,#a7a8ad 0%,#c6b8a2 40%,#c8ac8c 100%)}
.photo-car{background:linear-gradient(180deg,#c9b39a 0%,#b79f86 50%,#c9b49c 100%)}
.showcase-item p{margin-top:18px;color:var(--white);font-size:10px;line-height:13.5px}

/* profile */
.profile-photo{left:50px;top:772px;width:129px;height:194px;border:1px solid #ccc;background:linear-gradient(180deg,#6b6a4e 0%,#8d8c79 45%,#9a9a8c 100%)}
.profile-text{left:214px;top:769px;width:418px}
.profile-text h2{font-weight:600;font-size:12px;margin-bottom:8px}
.profile-text p{font-size:10px;line-height:13.5px;margin-bottom:11px;color:var(--ink)}

/* footer */
.site-footer{left:0;top:1002px;width:677px;height:163px;background:var(--navy)}
.footer-heading{top:22px;color:var(--white);font-weight:500;font-size:15.5px}
.footer-list{top:56px;list-style:none}
.footer-list li{color:var(--green);font-size:10px;line-height:14.6px}
.newsletter-label{left:479px;top:57px;color:var(--green);font-size:10px}
.newsletter-input{left:479px;top:71px;width:157px;height:21px;background:var(--white)}
.follow-label{left:479px;top:103px;color:var(--green);font-size:10px}
.social{top:118px;width:19px;height:19px}
.social.s1{left:479px;background:#3b5998}
.social.s2{left:503px;background:#2aa9e0}
.social.s3{left:527px;background:#0e76a8}
.social.s4{left:551px;background:#dd4b39}

/* bottom bar */
.bottom-bar{left:0;top:1165px;width:677px;height:35px;background:var(--charcoal)}
.copyright{left:48px;top:13px;color:#e6e6e6;font-size:6.5px}
.back-top{right:66px;top:13px;color:#e6e6e6;font-size:6.5px}
.back-top-icon{right:27px;top:9px}
</style>
</head>
<body>

<header class="site-header abs">
  <div class="brand abs">VORTAN<br>TACTICAL</div>
  <nav class="main-nav abs">
    <a href="#" class="active">HOME</a>
    <a href="#">ABOUT</a>
    <a href="#">EVENTS</a>
    <a href="#">NEWS</a>
    <a href="#">CONTACT</a>
  </nav>
</header>

<section class="hero abs">
  <div class="hero-photo" role="img" aria-label="Bomb technician in a protective suit kneeling beside a device in a desert compound"></div>
</section>
<div class="hero-caption abs">Lorem Ipsum is simply dummy text of the printing and typesetting industry. Lorem Ipsum has been the industry's standard dummy text ever since</div>
<div class="hero-arrow prev abs"><svg width="24" height="23"><polyline points="15,5 9,11.5 15,18" fill="none" stroke="#8cc63f" stroke-width="1.5"/></svg></div>
<div class="hero-arrow next abs"><svg width="24" height="23"><polyline points="9,5 15,11.5 9,18" fill="none" stroke="#8cc63f" stroke-width="1.5"/></svg></div>

<div class="feature abs" style="left:49px">
  <h3>What we do...</h3>
  <p>Lorem Ipsum is simply dummy text of the printing and typesetting industry. Lorem Ipsum has been the industry's standard dummy text ever since...</p>
  <span class="more-btn primary">more</span>
</div>
<div class="feature abs" style="left:256px">
  <h3>Upcoming events...</h3>
  <p>Lorem Ipsum is simply dummy text of the printing and typesetting industry. Lorem Ipsum has been the industry's standard dummy text ever since...</p>
  <span class="more-btn">more</span>
</div>
<div class="feature abs" style="left:464px">
  <h3>Our dedication...</h3>
  <p>Lorem Ipsum is simply dummy text of the printing and typesetting industry. Lorem Ipsum has been the industry's standard dummy text ever since...</p>
  <span class="more-btn">more</span>
</div>

<section class="showcase abs">
  <h2 class="showcase-title abs">Title can go here...</h2>
  <svg class="showcase-nav abs" style="left:584px" width="14" height="22"><polyline points="12,2 3,11 12,20" fill="none" stroke="#fff" stroke-width="1.6"/></svg>
  <svg class="showcase-nav abs" style="left:614px" width="14" height="22"><polyline points="2,2 11,11 2,20" fill="none" stroke="#fff" stroke-width="1.6"/></svg>
  <div class="showcase-item abs" style="left:49px">
    <div class="showcase-photo photo-blast" role="img" aria-label="Controlled detonation throwing debris across open desert"></div>
    <p>Lorem Ipsum is simply dummy text of the printing and typesetting industry. Lorem Ipsum has been the industry's standard dummy text ever since the 1500s, when an unknown printer took a galley of type and scrambled...</p>
  </div>
  <div class="showcase-item abs" style="left:374px">
    <div class="showcase-photo photo-car" role="img" aria-label="Vehicle explosion demonstration on a sandy training range"></div>
    <p>Lorem Ipsum is simply dummy text of the printing and typesetting industry. Lorem Ipsum has been the industry's standard dummy text ever since the 1500s, when an unknown printer took a galley of type and scrambled...</p>
  </div>
</section>

<div class="profile-photo abs" role="img" aria-label="Portrait of a uniformed instructor with arms crossed"></div>
<article class="profile-text abs">
  <h2>Title can go here...</h2>
  <p>Lorem Ipsum is simply dummy text of the printing and typesetting industry. Lorem Ipsum has been the industry's standard dummy text ever since the 1500s, when an unknown printer took a galley of type and scrambled it to make a type specimen book. It has survived not only five centuries, but also the leap into electronic typesetting, remaining essentially unchanged.</p>
  <p>It was popularised in the 1960s with the release of Typeline sheets containing Lorem Ipsum passages, and more recently with desktop publishing software like Quillset Layout including versions of Lorem Ipsum.</p>
  <p>Lorem Ipsum is simply dummy text of the printing and typesetting industry. Lorem Ipsum has been the industry's standard dummy text ever since the 1500s, when an unknown printer took a galley of type and scrambled it to make a type specimen book. It has survived not only five centuries, but also the leap into electronic typesetting, remaining essentially unchanged.</p>
</article>

<footer class="site-footer abs">
  <h3 class="footer-heading abs" style="left:48px">CONTACT US</h3>
  <ul class="footer-list abs" style="left:48px">
    <li>Company name</li><li>123 Road Name Here</li><li>Address Line</li><li>Address Line</li><li>Tel 01234 567890</li><li>Email name@yourdomain.com</li>
  </ul>
  <h3 class="footer-heading abs" style="left:250px">QUICK LINKS</h3>
  <ul class="footer-list abs" style="left:250px">
    <li>Home</li><li>Services</li><li>About us</li><li>Testimonials</li><li>FAQ's</li><li>Contact us</li>
  </ul>
  <ul class="footer-list abs" style="left:327px">
    <li>Terms of service</li><li>Sitemap</li><li>Privacy Policy</li><li>Another link</li><li>Another link</li><li>Another link</li>
  </ul>
  <h3 class="footer-heading abs" style="left:479px">NEWSLETTER</h3>
  <div class="newsletter-label abs">Sign up for our newsletter</div>
  <div class="newsletter-input abs"></div>
  <div class="follow-label abs">Follow us</div>
  <span class="social s1 abs"></span>
  <span class="social s2 abs"></span>
  <span class="social s3 abs"></span>
  <span class="social s4 abs"></span>
</footer>

<div class="bottom-bar abs">
  <div class="copyright abs">Copyright © 2014 Company name. All rights reserved. / Sitemap / Privacy / HTML Validation</div>
  <div class="back-top abs">Back to top</div>
  <svg class="back-top-icon abs" width="22" height="14"><polyline points="1,13 11,3 21,13" fill="none" stroke="#8cc63f" stroke-width="1.5"/></svg>
</div>

</body>
</html>
```